A website for Bloom Care, a multidisciplnary approach to treating development and functional issue

We need a simple, clean interface, that is intuitive.

We want parents to be able to be impressed by our services, and be able to trust our team and get simple easy to understand information about their child's potential condition and our therapists.

We also want the website to be mobile friendly and easy to integrate into social media as this will be how we attract people to our website.

Proper coding would be excellent too so that we have functionality and it can be easily changed

Target Market(s)

Parents, teachers, children, families

Number of Pages Required

5+ page

Font styles to use
Sans Serif

Colors
105da8
fbee3d
ec1f27

Requirements
Must have
• Social media functionality.
• Be bright simple and interesting.

```html
<!DOCTYPE html>
<html lang="en">
<head>
<meta charset="utf-8">
<title>Bloom Care</title>
<link href="https://fonts.googleapis.com/css2?family=Open+Sans:wght@400;600&family=Raleway:wght@300;400;500&family=Roboto+Condensed:wght@400&family=Lobster&display=swap" rel="stylesheet">
<style>
:root{
  --beige:#f1e9cd;
  --red:#d5121e;
  --blue:#1a4da0;
  --navy:#16397f;
  --ink:#333;
  --grey-bg:#f5f5f5;
  --cream:#fcfaf0;
  --footer-grey:#efefef;
  --dark:#262626;
  --white:#fff;
}
*{box-sizing:border-box;margin:0;padding:0}
html,body{width:670px;height:1200px;overflow:hidden;background:var(--white)}
body{font-family:"Open Sans",sans-serif;color:var(--ink);position:relative}
.abs{position:absolute}
.header-band{left:0;top:0;width:670px;height:332px;background:var(--beige)}
.brand{left:56px;top:46px;font-family:"Raleway",sans-serif;font-weight:500;font-size:22px;color:var(--ink);display:flex;align-items:center;gap:7px}
.brand-dot{width:14px;height:14px;border-radius:50%;background:var(--red)}
.social-top{left:406px;top:26px;display:flex;gap:5px}
.social-top span{width:16px;height:16px;border-radius:50%;background:var(--navy)}
.social-top span:nth-child(2){background:#2a9fd8}
.social-top span:nth-child(3){background:#444}
.social-top span:nth-child(4){background:#ef6c1f}
.social-top span:nth-child(5){background:var(--red)}
.hotline{left:516px;top:22px;display:flex;gap:8px;align-items:center}
.hotline-icon{width:22px;height:22px;border:1px solid #333;border-radius:50%;display:flex;align-items:center;justify-content:center}
.hotline-text{font-family:"Raleway",sans-serif;font-size:10px;line-height:14px;color:#222}
.main-nav{left:216px;top:66px;width:399px;height:32px;background:var(--red);border-radius:3px;display:flex;align-items:center;justify-content:space-around;font-family:"Roboto Condensed",sans-serif;font-size:9px;color:var(--white);text-transform:uppercase}
.main-nav span+span{border-left:1px solid rgba(255,255,255,.5);padding-left:14px}
.slider{left:55px;top:116px;width:560px;height:274px;background:var(--white);border-radius:4px;box-shadow:0 1px 3px rgba(0,0,0,.2)}
.slide-photo{left:60px;top:121px;width:550px;height:264px;background:linear-gradient(180deg,rgba(210,200,160,.6) 0%,rgba(0,0,0,0) 40%),linear-gradient(90deg,#9fb08a 0%,#7a6a55 25%,#3f7a55 45%,#d8a88e 65%,#df5a48 82%,#6fbfd8 100%)}
.slide-arrow{top:240px;width:18px;height:18px;border-radius:50%;background:rgba(30,30,30,.75);display:flex;align-items:center;justify-content:center}
.slide-caption{left:60px;top:344px;width:224px;height:41px;background:rgba(20,20,20,.75);font-family:"Lobster",sans-serif;font-size:24px;color:var(--white);padding:4px 10px}
.section-title{font-family:"Raleway",sans-serif;font-weight:300;color:#222}
.services-title{left:0;top:406px;width:670px;text-align:center;font-size:19px}
.services-intro{left:125px;top:434px;width:420px;text-align:center;font-size:6px;line-height:11px}
.service{top:470px;width:173px}
.service-photo{height:101px}
.service h3{font-family:"Raleway",sans-serif;font-weight:400;font-size:8px;margin-top:14px;color:#222}
.service p{font-size:6px;line-height:11.5px;margin-top:6px}
.read-more{font-size:7px;font-weight:600;color:var(--navy);text-decoration:underline;margin-top:8px;display:block}
.welcome-band{left:0;top:674px;width:670px;height:200px;background:var(--grey-bg)}
.welcome-title{left:56px;top:689px;font-size:19px;font-weight:400}
.welcome-title em{font-style:normal;color:var(--blue)}
.welcome-photo{left:54px;top:726px;width:146px;height:127px;background:linear-gradient(180deg,#c9cfa0 0%,#e7b89a 45%,#d8555a 75%,#e9c444 100%)}
.welcome-text{left:214px;top:725px;width:232px;font-size:6px;line-height:11.6px}
.welcome-text p+p{margin-top:5px}
.welcome-more{left:211px;top:845px;font-family:"Raleway",sans-serif;font-size:8px;display:flex;gap:4px;align-items:center}
.appointment{left:469px;top:674px;width:146px;height:200px;background:#f2f2f2;border:1px solid #e5e5e5}
.appointment-head{height:54px;background:var(--red);color:var(--white);text-align:center;font-family:"Raleway",sans-serif;padding-top:8px}
.appointment-head .t{font-size:11px}
.appointment-head .n{font-size:11px;font-weight:500;margin-top:3px;display:flex;align-items:center;justify-content:center;gap:3px}
.or-badge{left:534px;top:719px;width:18px;height:18px;border-radius:50%;background:var(--white);color:var(--red);font-size:7px;font-weight:600;display:flex;align-items:center;justify-content:center}
.field{left:476px;width:130px;height:22px;background:var(--white);border:1px solid #e2e2e2;font-size:5.5px;color:#888;padding:7px 8px}
.submit{left:476px;top:837px;width:130px;height:21px;background:var(--blue);border-radius:2px;color:var(--white);font-size:8px;text-align:center;line-height:21px}
.testimonial-band{left:0;top:874px;width:670px;height:174px;background:var(--cream)}
.therapists-photo{left:54px;top:900px;width:163px;height:122px;background:linear-gradient(180deg,#d8cdb0 0%,#a89a80 40%,#7a5a55 70%,#2f4f8a 100%)}
.therapists-label{left:54px;top:1002px;width:163px;text-align:center;font-family:"Raleway",sans-serif;font-size:11px;color:var(--white)}
.testimonial-title{left:242px;top:904px;font-size:11px;font-weight:400;text-transform:uppercase}
.avatar{left:242px;top:939px;width:66px;height:66px;border-radius:50%;background:radial-gradient(circle at 50% 40%,#b9a594,#4a4f58 70%,#2a2f38)}
.quote{left:319px;top:942px;width:298px;font-size:6px;line-height:11.5px;font-style:italic}
.quote-name{left:319px;top:995px;font-family:"Raleway",sans-serif;font-size:8px;color:var(--navy)}
.footer-left{left:0;top:1048px;width:214px;height:118px;background:var(--footer-grey)}
.footer-brand{left:0;top:1098px;width:214px;justify-content:center}
.footer-main{left:214px;top:1048px;width:456px;height:118px;background:var(--blue)}
.footer-col{top:1066px;color:var(--white)}
.footer-col h4{font-family:"Raleway",sans-serif;font-weight:400;font-size:9.5px;text-transform:uppercase;margin-bottom:9px}
.footer-col li{list-style:none;font-size:6.5px;line-height:12.5px;display:flex;align-items:center;gap:6px}
.footer-col .dot{width:5px;height:5px;border-radius:50%;background:var(--white)}
.bottom-bar{left:0;top:1166px;width:670px;height:34px;background:var(--dark);color:var(--white);font-size:6px;display:flex;align-items:center;justify-content:space-between;padding:0 55px}
</style>
</head>
<body>
<div class="abs header-band"></div>

<div class="abs brand"><span class="brand-dot"></span>Bloom Care</div>

<div class="abs social-top" aria-label="Social links"><span></span><span></span><span></span><span></span><span></span></div>

<div class="abs hotline">
  <div class="hotline-icon"><svg width="10" height="10" viewBox="0 0 24 24"><path d="M6.6 10.8a15 15 0 0 0 6.6 6.6l2.2-2.2a1 1 0 0 1 1-.25 11.4 11.4 0 0 0 3.6.57 1 1 0 0 1 1 1V20a1 1 0 0 1-1 1A17 17 0 0 1 3 4a1 1 0 0 1 1-1h3.5a1 1 0 0 1 1 1c0 1.25.2 2.45.57 3.57a1 1 0 0 1-.25 1z" fill="#222"/></svg></div>
  <div class="hotline-text">HOT LINE:<br>+91-300-555-0142</div>
</div>

<nav class="abs main-nav"><span>Home</span><span>About Us</span><span>Our Services</span><span>Events</span><span>Our Therapists</span><span>Contact Us</span></nav>

<div class="abs slider"></div>
<div class="abs slide-photo" role="img" aria-label="Therapist smiling with three children working together at a classroom table"></div>
<div class="abs slide-arrow" style="left:77px"><svg width="8" height="8" viewBox="0 0 8 8"><path d="M5 1L2 4l3 3" stroke="#fff" stroke-width="1.4" fill="none"/></svg></div>
<div class="abs slide-arrow" style="left:574px;background:#111"><svg width="8" height="8" viewBox="0 0 8 8"><path d="M3 1l3 3-3 3" stroke="#fff" stroke-width="1.4" fill="none"/></svg></div>
<div class="abs slide-caption">bloom care center</div>

<h2 class="abs section-title services-title">our services</h2>
<p class="abs services-intro">Lorem ipsum dolor sit amet conse ctetur adipisicing elit, sed do eiusmod tempor incididunt ut labore et dolore magna aliqua. Ut enim ad minim veniam, quis nostrud exercitation ullamco laboris nisi ut aliquip ex ea commodo consequat. Duis aute irure</p>

<div class="abs service" style="left:54px">
  <div class="service-photo" role="img" aria-label="Children playing with building blocks on a playroom floor" style="background:linear-gradient(180deg,#d9c7a8 0%,#b9a27f 45%,#4f86b8 70%,#c98a5a 100%)"></div>
  <h3>DOLOR SIT AMET CONSE CTETUR</h3>
  <p>Lorem ipsum dolor sit amet, consectetur adipisicing elit, sed do eiusmod tempor incididunt ut labore et dolore magna Lorem ipsum dolor sit amet,</p>
  <span class="read-more">READ MORE</span>
</div>
<div class="abs service" style="left:249px">
  <div class="service-photo" role="img" aria-label="Young child drawing at a desk with a helper beside her" style="background:linear-gradient(180deg,#f2e6dc 0%,#eab7a0 40%,#e56aa8 65%,#c8966a 100%)"></div>
  <h3>DOLOR SIT AMET CONSE CTETUR</h3>
  <p>Lorem ipsum dolor sit amet, consectetur adipisicing elit, sed do eiusmod tempor incididunt ut labore et dolore magna Lorem ipsum dolor sit amet,</p>
  <span class="read-more">READ MORE</span>
</div>
<div class="abs service" style="left:442px">
  <div class="service-photo" role="img" aria-label="Children playing a floor game on a colourful dotted mat" style="background:linear-gradient(180deg,#a6836a 0%,#d47a9a 40%,#efe7ea 70%,#d84a55 100%)"></div>
  <h3>DOLOR SIT AMET CONSE CTETUR</h3>
  <p>Lorem ipsum dolor sit amet, consectetur adipisicing elit, sed do eiusmod tempor incididunt ut labore et dolore magna Lorem ipsum dolor sit amet,</p>
  <span class="read-more">READ MORE</span>
</div>

<div class="abs welcome-band"></div>
<h2 class="abs section-title welcome-title">Welcome To <em>bloom care</em></h2>
<div class="abs welcome-photo" role="img" aria-label="Therapist and little girl building with toy bricks"></div>
<div class="abs welcome-text">
  <p>Lorem ipsum dolor sit amet, consectetur adipiscing elit, sed do eiusmod tempor incididunt ut labore et dolore magna aliqua. Ut enim ad minim veniam, quis nostrud exercitation Lorem ipsum dolor sit amet, consectetur adipiscing elit, sed do eiusmod tempor incididunt ut labore et dolore magna aliqua. Ut enim ad minim veniam, quis nostrud exercitation</p>
  <p>Lorem ipsum dolor sit amet, consectetur adipiscing elit, sed do eiusmod tempor incididunt ut labore et dolore magna aliqua. Ut enim ad minim veniam, quis nostrud exercitation Lorem ipsum dolor sit amet, consectetur adipiscing elit, sed do eiusmod tempor incididunt ut labore</p>
</div>
<div class="abs welcome-more">READ MORE <svg width="8" height="8" viewBox="0 0 8 8"><circle cx="4" cy="4" r="4" fill="#222"/><path d="M3.3 2.2L5 4 3.3 5.8" stroke="#fff" stroke-width="1.1" fill="none"/></svg></div>

<aside class="abs appointment">
  <div class="appointment-head">
    <div class="t">Make an Appointment</div>
    <div class="n"><svg width="8" height="10" viewBox="0 0 8 10" aria-hidden="true"><rect x="0.6" y="0.6" width="6.8" height="8.8" rx="1" fill="none" stroke="#fff" stroke-width="1.1"/><rect x="2" y="2" width="4" height="3.2" fill="#fff"/><circle cx="2.4" cy="7" r=".6" fill="#fff"/><circle cx="4" cy="7" r=".6" fill="#fff"/><circle cx="5.6" cy="7" r=".6" fill="#fff"/></svg>1-800-555-0199</div>
  </div>
</aside>
<div class="abs or-badge">OR</div>
<div class="abs field" style="top:747px">Name</div>
<div class="abs field" style="top:777px">Phone No</div>
<div class="abs field" style="top:806px">E Mail</div>
<div class="abs submit">SUBMIT REQUEST</div>

<div class="abs testimonial-band"></div>
<div class="abs therapists-photo" role="img" aria-label="Teacher with a group of children raising hands in a classroom"></div>
<div class="abs therapists-label">Our Therapists</div>
<h2 class="abs section-title testimonial-title">What our patients say</h2>
<div class="abs avatar" role="img" aria-label="Portrait of a parent giving a testimonial"></div>
<p class="abs quote">&ldquo; Lorem ipsum dolor sit amet, consectetur adipiscing elit, sed do eiusmod tempor incididunt ut labore et dolore magna aliqua. Ut enim ad minim veniam, quis nostrud exercitation ullamco laboris nisi ut aliquip ex ea commodo consequat. Lorem ipsum dolor sit amet, consectetur adipiscing elit, sed do eiusmod tempor incididunt ut labore et dolore magna aliqua.</p>
<div class="abs quote-name">SAM PORTER</div>

<div class="abs footer-left"></div>
<div class="abs brand footer-brand"><span class="brand-dot"></span>Bloom Care</div>
<div class="abs footer-main"></div>
<div class="abs footer-col" style="left:235px">
  <h4>Our Features</h4>
  <ul><li>Lorem Ipsum Dolor</li><li>Excepteur Sint Officia Deserunt</li><li>Cupidatat Proident</li><li>Officia Deserunt Officia Deserunt</li></ul>
</div>
<div class="abs footer-col" style="left:372px">
  <h4>Contact Us</h4>
  <ul>
    <li>4120 Bloom Care Maple Lane ,</li><li>PO Box 2200, Brookfield</li>
    <li style="margin-top:5px"><svg width="9" height="9" viewBox="0 0 24 24"><path d="M6.6 10.8a15 15 0 0 0 6.6 6.6l2.2-2.2a1 1 0 0 1 1-.25 11.4 11.4 0 0 0 3.6.57 1 1 0 0 1 1 1V20a1 1 0 0 1-1 1A17 17 0 0 1 3 4a1 1 0 0 1 1-1h3.5a1 1 0 0 1 1 1c0 1.25.2 2.45.57 3.57a1 1 0 0 1-.25 1z" fill="none" stroke="#fff" stroke-width="1.6"/></svg>1-800-555-0173</li>
    <li><svg width="9" height="9" viewBox="0 0 12 12"><rect x="1" y="2.5" width="10" height="7" fill="none" stroke="#fff"/><path d="M1 2.5l5 4 5-4" fill="none" stroke="#fff"/></svg>hello@bloomcare.org</li>
  </ul>
</div>
<div class="abs footer-col" style="left:544px">
  <h4>Social Media</h4>
  <ul><li><span class="dot"></span>Friendsy</li><li><span class="dot"></span>Chirper</li><li><span class="dot"></span>Circles</li><li><span class="dot"></span>ClipTube</li></ul>
</div>

<footer class="abs bottom-bar"><span>&copy;2014 - 2015 bloom care center., All Rights Reserved.</span><span>Terms of Service | Privacy Policy</span></footer>
</body>
</html>
```